Corporate Identity Design Project

Teslin Varrow Design is a small boutique event planning and floral design company, based in Northern Alberta. I require the creation of some corporate identity pieces. I want a minimalistic design.
Website www.teslinvarrow.example

Pieces should include
1. Business Card
Should include the company logo, name, email address, address, phone number. These will be professional printed.
These are three cards that I like:
http://cardsamplegallery.example/wp-content/uploads/2010/02/Odile_Vantreck_Roomworks_by_Pepperleaf_studio_Media.jpg
http://neatcardshowcase.example/wp-content/uploads/2011/06/Quiet-Studio-Minimalist-Business-Cards_11.jpg
http://graphicfeedhub.example/wp-content/uploads/2012/03/16.minimalist-business-cards.jpg
I like letterpress, but I am open to other options.

2. Letterhead
will be professionally printed

3. Envelope

4. Fax Sheet
will be printed on home printer

5. Pocket Presentation
Like -http://wrenfieldgardens.example/img/design_step_proposal@2x.jpg

6. Invoice
Like - http://samplehost.example/quillmarsh/2011/02/falcon-athletics-4-letterhead-combined.png?w=529

7. Proposal
Like something like this – this will not be printed, but rather emailed to clients
Like http://files7.imagedepot.example/getfile/files.imagedepot.example/trelvo-studio/nkuBfi2LVj7ENiUb5D16wqAHQHqNNT5vut7mukSTmisfoGHYXGEv9haEQOPL/Picture-52.png.scaled.500.jpg

8. Contract
Like http://www.brightkeyadvertising.example/images/sample-contract.jpg

9. Business Brochure – I have removed this piece from the project and will most likely post it as another project at a later date.

If you think that this is a project of interest to you, but feel that it is “too much” work for the price, please let me know how you would re-package it – I am open to suggestions.

Target Market(s)

Young women

Industry/Entity Type

Boutique

Requirements
Should not have
• I do not want it to look "frilly"

```html
<!DOCTYPE html>
<html lang="en">
<head>
<meta charset="utf-8">
<title>Teslin Varrow Design — Stationery Set</title>
<link rel="stylesheet" href="https://fonts.googleapis.com/css2?family=PT+Sans:wght@400;700&family=Ubuntu:wght@400;500&display=swap">
<style>
:root{
  --backdrop:#dbd3cf;
  --backdrop-light:#ece8e6;
  --charcoal:#4a4a44;
  --charcoal-loop:#6a6a64;
  --rose:#b5696d;
  --ink:#2f2f2f;
  --muted:#5a5a5a;
  --band:#c9c7c4;
  --paper:#ffffff;
  --loop:#e4e4e4;
}
*{box-sizing:border-box;margin:0;padding:0}
html,body{width:1200px;height:900px;overflow:hidden}
body{
  position:relative;
  background:radial-gradient(ellipse at 50% 48%,var(--backdrop-light) 0%,var(--backdrop) 60%);
  font-family:"PT Sans",Arial,sans-serif;color:var(--ink);
}
.piece{position:absolute}
.label{position:absolute;font-size:11px;letter-spacing:.5px;color:#555;white-space:nowrap}

/* wordmark stand-in */
.wordmark{display:flex;align-items:center;gap:8px;font-family:"Ubuntu",sans-serif;font-weight:500;color:var(--charcoal);letter-spacing:1.5px;line-height:1.05;text-transform:uppercase;white-space:nowrap}
.wordmark .dot{border-radius:50%;background:var(--rose);flex:none}
.wordmark.light{color:#fff}

.loops{position:absolute;background:var(--loop);opacity:.6;border-radius:50%}

/* business cards */
.card{width:192px;height:112px;border-radius:10px;overflow:hidden;box-shadow:0 2px 4px rgba(0,0,0,.25)}
.card-back{left:103px;top:58px;background:var(--charcoal)}
.card-back .loops{background:var(--charcoal-loop);opacity:.7;left:-10px;top:-8px;width:170px;height:100px}
.card-back .wordmark{position:absolute;right:14px;top:70px;font-size:7px}
.card-back .tagline{position:absolute;left:10px;top:95px;font-size:3.6px;color:#bbb;letter-spacing:.4px;white-space:nowrap}
.card-front{left:330px;top:58px;background:var(--paper)}
.card-front .loops{left:-10px;top:0;width:90px;height:112px}
.card-front .wordmark{position:absolute;left:22px;top:44px;font-size:6px}
.card-front .person{position:absolute;left:117px;top:22px}
.card-front .person h3{font-size:8px;font-weight:400;color:var(--ink)}
.card-front .person .role{font-size:5px;color:var(--rose);font-style:italic}
.card-front .details{position:absolute;left:117px;top:53px;font-size:4.3px;line-height:6.3px;color:var(--muted);white-space:nowrap}
.card-front .details .co{color:var(--rose)}
.sq{display:inline-block;width:4px;height:4px;background:var(--rose);margin-right:2px;vertical-align:-0.5px}

/* fax */
.fax{left:82px;top:218px;width:459px;height:590px;background:var(--paper);box-shadow:0 1px 4px rgba(0,0,0,.2);overflow:hidden}
.fax .site{position:absolute;right:18px;top:16px;font-size:7px;color:var(--rose)}
.fax .head{position:absolute;left:26px;top:52px;display:flex;align-items:center;gap:4px}
.fax .head .wordmark{font-size:13px}
.fax .head .title{font-family:"Ubuntu",sans-serif;font-weight:500;font-size:28px;color:var(--rose)}
.fax .fields{position:absolute;left:0;top:106px;width:459px;height:88px;background:var(--band);display:grid;grid-template-columns:197px 1fr;padding:12px 0 0 35px;row-gap:10px;font-size:11px;color:#444}
.fax .fields span b{font-weight:400;margin-left:14px}
.fax .loops{right:-30px;top:460px;width:160px;height:150px}
.footer{position:absolute;display:flex;gap:8px;font-size:7.5px;line-height:11px;color:#333;white-space:nowrap}
.footer .co{position:absolute;top:-13px;left:0;font-size:6px;color:var(--rose)}
.footer .contact{border-left:1px solid var(--rose);padding-left:6px}
.footer .phone{font-size:9px}
.fax .footer{left:16px;top:560px}

/* letterhead back */
.lh-back{left:628px;top:228px;width:502px;height:650px;background:var(--charcoal);box-shadow:0 2px 6px rgba(0,0,0,.3);overflow:hidden}
.lh-back .loops{background:var(--charcoal-loop);left:-30px;top:90px;width:110px;height:260px;opacity:.8}
.lh-back .wordmark{position:absolute;left:330px;top:582px;font-size:12px}
.lh-back .tagline{position:absolute;left:25px;top:610px;font-size:8px;color:#ddd;letter-spacing:.6px;white-space:nowrap}

/* letterhead front */
.lh-front{left:683px;top:140px;width:460px;height:650px;background:var(--paper);box-shadow:0 2px 8px rgba(0,0,0,.3);overflow:hidden}
.lh-front .band{position:absolute;left:0;width:460px;background:linear-gradient(#fff,#e2e2e2)}
.lh-front .site{position:absolute;right:20px;top:12px;font-size:7px;color:var(--rose)}
.lh-front > .wordmark{position:absolute;left:12px;top:42px;font-size:13px}
.lh-front .meta{position:absolute;left:20px;top:149px;width:66px;text-align:right;font-size:7px;line-height:9px}
.lh-front .meta dt{color:var(--rose);font-size:8px;margin-top:6px}
.lh-front .meta dd{color:#444}
.lh-front .letter{position:absolute;left:132px;top:149px;width:276px;font-size:6.1px;line-height:10.4px;color:#222;text-align:justify}
.lh-front .letter p{margin-bottom:11px}
.lh-front .sign{width:80px;height:24px;background:#eee;border-radius:3px;margin:6px 0 4px -16px}
.lh-front .loops{right:-30px;top:480px;width:170px;height:160px}
.lh-front .footer{left:20px;top:626px}
</style>
</head>
<body>

<div class="piece" style="right:28px;top:44px">
  <div class="wordmark" style="font-size:15px"><span class="dot" style="width:22px;height:22px"></span>Teslin Varrow<br>Design</div>
</div>

<span class="label" style="left:540px;top:62px">Business Card</span>
<span class="label" style="left:580px;top:143px">Letterhead Front</span>
<span class="label" style="left:271px;top:821px">Fax Sheet</span>
<span class="label" style="left:530px;top:867px">Letterhead Back</span>

<section class="piece card card-back">
  <div class="loops" role="img" aria-label="Faint looping brand decoration"></div>
  <div class="wordmark light"><span class="dot" style="width:9px;height:9px"></span>Teslin Varrow<br>Design</div>
  <p class="tagline">WEDDING INSPIRATION · LAKE ORVEN · MARLSTOCK · FLORAL DESIGN</p>
</section>

<section class="piece card card-front">
  <div class="loops" role="img" aria-label="Faint looping brand decoration"></div>
  <div class="wordmark"><span class="dot" style="width:8px;height:8px"></span>Teslin Varrow<br>Design</div>
  <div class="person"><h3>Teslin Varrow</h3><p class="role">Designer</p></div>
  <div class="details">
    <p class="co">Teslin Varrow Design</p>
    <p>Office, Floor #, Building,</p>
    <p>Street, City, Country XXXX</p>
    <p><span class="sq"></span>010-555-0142</p>
    <p><span class="sq"></span>hello@teslinvarrow.example</p>
    <p><span class="sq"></span>@teslinvarrow</p>
  </div>
</section>

<section class="piece fax">
  <p class="site">teslinvarrow.example</p>
  <div class="head">
    <div class="wordmark"><span class="dot" style="width:30px;height:30px"></span>Teslin Varrow<br>Design</div>
    <span class="title">FAX</span>
  </div>
  <div class="fields">
    <span>Date<b>:</b></span><span>Regarding<b>:</b></span>
    <span>Attention<b>:</b></span><span>Pages<b>:</b></span>
    <span>From<b>:</b></span><span>Including cover<b>:</b></span>
  </div>
  <div class="loops" role="img" aria-label="Faint looping brand decoration"></div>
  <div class="footer">
    <span class="co">Teslin Varrow Design</span>
    <p>Office, FLoor #, Building,<br>Street, City, Country XXXX</p>
    <p class="contact"><span class="phone">010-555-0142</span><br>hello@teslinvarrow.example</p>
  </div>
</section>

<section class="piece lh-back">
  <div class="loops" role="img" aria-label="Faint looping brand decoration"></div>
  <div class="wordmark light"><span class="dot" style="width:20px;height:20px"></span>Teslin Varrow<br>Design</div>
  <p class="tagline">WEDDING INSPIRATION | LAKE ORVEN | MARLSTOCK | FLORAL DESIGN</p>
</section>

<section class="piece lh-front">
  <div class="band" style="top:143px;height:72px"></div>
  <div class="band" style="top:365px;height:68px"></div>
  <p class="site">teslinvarrow.example</p>
  <div class="wordmark"><span class="dot" style="width:34px;height:34px"></span>Teslin Varrow<br>Design</div>
  <dl class="meta">
    <dt>Subject</dt><dd>Lorem Ipsum</dd>
    <dt>Date</dt><dd>01/02/2012</dd>
    <dt>Receiver</dt><dd>Mara Quill</dd>
  </dl>
  <div class="loops" role="img" aria-label="Faint looping brand decoration"></div>
  <article class="letter">
    <p>Dear Client,</p>
    <p>Lorem ipsum dolor sit amet, consectetur adipisicing elit, sed do eiusmod tempor incididunt ut labore et dolore magna aliqua. Ut enim ad minim veniam, quis nostrud exercitation ullamco laboris nisi ut aliquip ex ea commodo consequat. Duis aute irure dolor in reprehenderit in voluptate velit esse cillum dolore eu fugiat nulla pariatur. Excepteur sint occaecat cupidatat non proident, sunt in culpa qui officia deserunt mollit anim id est laborum.</p>
    <p>Lorem ipsum dolor sit amet, consectetur adipisicing elit, sed do eiusmod tempor incididunt ut labore et dolore magna aliqua. Ut enim ad minim veniam, quis nostrud exercitation ullamco laboris nisi ut aliquip ex ea commodo consequat. Duis aute irure dolor in reprehenderit in voluptate velit esse cillum dolore eu fugiat nulla pariatur. Excepteur sint occaecat cupidatat non proident, sunt in culpa qui officia deserunt mollit anim id est laborum.</p>
    <p>Lorem ipsum dolor sit amet, consectetur adipisicing elit, sed do eiusmod tempor incididunt ut labore et dolore magna aliqua. Ut enim ad minim veniam, quis nostrud exercitation ullamco laboris nisi ut aliquip ex ea commodo consequat. Duis aute irure dolor in reprehenderit in voluptate velit esse cillum dolore eu fugiat nulla pariatur. Excepteur sint occaecat cupidatat non proident, sunt in culpa qui officia deserunt mollit anim id est laborum.</p>
    <p>Lorem ipsum dolor sit amet, consectetur adipisicing elit, sed do eiusmod tempor incididunt ut labore et dolore magna aliqua. Ut enim ad minim veniam, quis nostrud exercitation ullamco laboris nisi ut aliquip ex ea commodo consequat. Duis aute irure dolor in reprehenderit in voluptate velit esse cillum dolore eu fugiat nulla pariatur. Excepteur sint occaecat cupidatat non proident, sunt in culpa qui officia deserunt mollit anim id est laborum.</p>
    <p>Lorem ipsum dolor sit amet, consectetur adipisicing elit, sed do eiusmod tempor incididunt ut labore et dolore magna aliqua. Ut enim ad minim veniam, quis nostrud exercitation ullamco laboris nisi ut aliquip ex ea commodo consequat. Duis aute irure dolor in reprehenderit in voluptate velit esse cillum dolore eu fugiat nulla pariatur. Excepteur sint occaecat cupidatat non proident, sunt in culpa qui officia deserunt mollit anim id est laborum.</p>
    <p style="margin-bottom:0">Yours Sincerely,</p>
    <div class="sign" role="img" aria-label="Handwritten signature"></div>
    <p style="line-height:9px">Rowan Pell<br>Executive manager</p>
  </article>
  <div class="footer">
    <span class="co">Teslin Varrow Design</span>
    <p>Office, FLoor #, Building,<br>Street, City, Country XXXX</p>
    <p class="contact"><span class="phone">010-555-0142</span><br>hello@teslinvarrow.example</p>
  </div>
</section>

</body>
</html>
```